professional looking data specialist website

I've recently had a new logo designed and I'm now looking to get a professional looking website built. This is for a new company that specialises in data. We look to support companies with business intelligence, report modelling, data governance to new european legislation (GDPR). We are offer consultancy or we can attend site and complete work when required. Our target arket is united kingdom wide and we are specifically aiming at small to medium sized companies.

Target Market(s)

small to medium enterprise companies from all industries

Industry/Entity Type

Professional Service

Coding

Coded - Design and coding required

Number of Pages Required

4 page

Font styles to use
Sans Serif

Colors

Designer to choose colors to be used in the design.

Requirements
Must have
• Professional look including the company logo, need to have ability to request more information from us so needs a inquiries page, seperate pages for the different offerings, data governance, report modelling, business intelligence implementation, data protection
Nice to have
• any website interaction, animation, etc
Should not have
• too many colours, too busy pages, must look professional

```html
<!DOCTYPE html>
<html lang="en">
<head>
<meta charset="utf-8">
<title>Harlow Data – Data Governance Specialists</title>
<link href="https://fonts.googleapis.com/css2?family=Roboto:ital,wght@0,300;0,400;0,500;0,700;1,400&family=Oswald:wght@400;500&display=swap" rel="stylesheet">
<style>
:root{
  --blue:#1a73c1;
  --blue-dark:#0e5a9a;
  --band:#1c6aae;
  --navy:#0b3553;
  --navy-bar:#0e4a77;
  --ink:#333;
  --muted:#666;
  --light:#f2f2f2;
  --line:#8db4d8;
  --white:#fff;
}
*{margin:0;padding:0;box-sizing:border-box}
html,body{width:693px;height:1200px;overflow:hidden}
body{position:relative;font-family:"Roboto",Arial,sans-serif;color:var(--ink);background:var(--white)}
.abs{position:absolute}

/* header */
.site-header{left:0;top:0;width:693px;height:62px;background:#f5f5f5;border-top:3px solid var(--blue);border-bottom:1px solid #ddd}
.nav-link{top:28px;font-size:8px;color:#222;text-transform:uppercase;letter-spacing:.2px}
.nav-link.active{color:var(--blue)}
.brand{left:306px;top:17px;width:80px;text-align:center}
.brand-mark{display:block;width:14px;height:14px;background:var(--blue);margin:0 auto 3px}
.brand-name{font-size:12px;color:var(--blue);font-weight:400}

/* hero */
.hero{left:0;top:62px;width:693px;height:256px;background:linear-gradient(90deg,#8e9aa3 0%,#c9d0d4 35%,#b9bfb8 60%,#d5dad6 100%)}
.hero-shade{left:0;top:62px;width:693px;height:256px;background:rgba(40,40,40,.18)}
.hero-kicker{left:0;width:693px;top:148px;text-align:center;color:#fff;font-size:10px;font-weight:300}
.hero-title{left:0;width:693px;top:160px;text-align:center;color:#fff;font-size:29px;font-weight:700;letter-spacing:-.5px}
.hero-text{left:128px;width:437px;top:194px;text-align:center;color:#fff;font-size:7px;line-height:10px}
.hero-arrow{top:172px;width:28px;height:26px;background:#f3f3f3;display:flex;align-items:center;justify-content:center}

/* welcome */
.welcome{left:0;top:318px;width:346px;height:204px;background:var(--light)}
.welcome-kicker{left:94px;top:345px;font-size:9px;color:#333}
.welcome-name{left:93px;top:354px;font-size:22px;color:var(--blue);font-weight:400}
.welcome-mark{left:210px;top:340px;width:11px;height:11px;background:var(--blue)}
.welcome-rule{left:94px;top:386px;width:238px;height:1px;background:#d8d8d8}
.welcome-text{left:94px;top:396px;width:242px;font-size:6.6px;line-height:10px;color:#555}
.contact-box{left:93px;top:458px;width:238px;height:41px;border:1px solid var(--line);background:#f7f7f7}
.contact-icon{width:28px;height:24px;border:1.5px solid var(--blue);display:flex;align-items:center;justify-content:center}
.contact-label{font-size:9px;color:var(--blue-dark)}
.contact-value{font-size:12px;color:var(--blue);font-weight:500;font-family:"Oswald",sans-serif}

/* quote */
.quote{left:346px;top:318px;width:347px;height:204px;background:linear-gradient(135deg,#2f86d2,#1a6fbf 60%,#3c8fd6)}
.quote-title{left:366px;top:338px;font-size:13px;color:#fff}
.quote-sub{left:366px;top:355px;font-size:7px;color:#e6f0fa;letter-spacing:.3px}
.field{left:366px;width:232px;border:1px solid rgba(255,255,255,.75);color:#e9f2fb;font-size:6px;padding:4px 6px}
.submit{left:366px;top:490px;width:52px;height:20px;border:1px solid #fff;background:var(--blue-dark);color:#fff;font-family:"Oswald",sans-serif;font-size:10px;display:flex;align-items:center;justify-content:center}

/* section heading */
.section-title{left:0;width:693px;text-align:center;font-size:19px;color:#333;font-weight:400}
.title-line{height:1px;background:var(--blue)}
.title-sq{width:10px;height:10px;background:#7fb1dc}
.title-under{left:333px;width:28px;height:1px;background:#ccc}

/* services */
.card{top:592px;width:124px;height:98px;border:1px solid #9bb8d6;background:#fff;text-align:center}
.card-icon{position:absolute;left:46px;top:10px;width:32px;height:32px;background:var(--blue);display:flex;align-items:center;justify-content:center}
.card-title{position:absolute;left:0;width:100%;top:52px;font-size:10px;color:#222}
.card-rule{position:absolute;left:6px;right:6px;top:67px;height:1px;background:#ccc}
.card-text{position:absolute;left:6px;right:6px;top:70px;font-size:6px;line-height:8px;color:#555}
.divider{left:0;top:704px;width:693px;height:1px;background:#b7d3ea}

/* band */
.cta{left:0;top:722px;width:693px;height:70px;background:var(--band)}
.cta-icon{left:197px;top:740px;width:32px;height:33px;border:1.5px solid #fff;display:flex;align-items:center;justify-content:center}
.cta-title{left:238px;top:731px;font-family:"Oswald",sans-serif;font-size:26px;color:#fff;letter-spacing:-.5px}
.cta-sub{left:239px;top:765px;font-size:12px;color:#fff;font-weight:300}

/* testimonials */
.testimonial{top:866px;width:226px;height:75px;border:1px solid #a9c6e0;background:var(--light)}
.quote-mark{top:858px;font-family:"Oswald",sans-serif;font-size:28px;color:var(--blue);line-height:1}
.testimonial-text{top:885px;width:196px;font-size:6.5px;line-height:10px;font-style:italic;color:#555}
.avatar{width:38px;height:38px;border-radius:50%;border:2px solid var(--blue);background:linear-gradient(#d9c2ad,#b98f72)}
.person{font-size:10px;color:#222}
.role{font-size:6px;color:#999}

/* footer */
.footer{left:0;top:1016px;width:693px;height:162px;background:var(--navy)}
.footer-bar{left:0;top:1178px;width:693px;height:22px;background:var(--navy-bar);color:#fff;font-size:6.5px;text-align:center;line-height:22px}
.footer-head{top:1041px;font-size:10px;color:#fff}
.footer-rule{height:1px;background:#4f6f89}
.footer-text{font-size:5.8px;line-height:9px;color:#fff}
.footer-item{left:292px;font-size:10px;color:#fff;display:flex;align-items:center;gap:6px}
.footer-item small{font-size:6.5px}
.social{top:1139px;width:13px;height:13px;border-radius:50%;background:#1a7fd0}
.news-input{left:467px;top:1070px;width:132px;height:24px;background:#c7d1d8;font-size:6px;color:#555;padding:8px 7px}
.subscribe{left:467px;top:1103px;width:55px;height:17px;background:var(--blue);color:#fff;font-size:7px;font-weight:700;display:flex;align-items:center;justify-content:center}
</style>
</head>
<body>

<header class="site-header abs">
  <span class="nav-link abs active" style="left:92px">Home</span>
  <span class="nav-link abs" style="left:145px">Who we are</span>
  <span class="nav-link abs" style="left:229px">What we offer</span>
  <div class="brand abs"><span class="brand-mark"></span><span class="brand-name">Harlow Data</span></div>
  <span class="nav-link abs" style="left:397px">Features</span>
  <span class="nav-link abs" style="left:469px">What we think</span>
  <span class="nav-link abs" style="left:563px">Contact</span>
</header>

<section>
  <div class="hero abs" role="img" aria-label="Photo of data charts on a screen with business people walking in an office"></div>
  <div class="hero-shade abs"></div>
  <p class="hero-kicker abs">HARLOW DATA, SPECIALIZES IN</p>
  <h1 class="hero-title abs">DATA GOVERNANCE (GDPR)</h1>
  <p class="hero-text abs">Lorem Ipsum is simply dummy text of the printing and typesetting industry. Lorem Ipsum has been the industry's standard dummy text ever since the 1500s, when an unknown printer took a galley of type and scrambled.</p>
  <div class="hero-arrow abs" style="left:8px"><svg width="8" height="8" viewBox="0 0 8 8"><path d="M5.5 1 2.5 4 5.5 7" fill="none" stroke="#222" stroke-width="1.3"/></svg></div>
  <div class="hero-arrow abs" style="left:655px"><svg width="8" height="8" viewBox="0 0 8 8"><path d="M2.5 1 5.5 4 2.5 7" fill="none" stroke="#222" stroke-width="1.3"/></svg></div>
</section>

<section>
  <div class="welcome abs"></div>
  <p class="welcome-kicker abs">WELCOME TO</p>
  <h2 class="welcome-name abs">Harlow Data</h2>
  <div class="welcome-rule abs"></div>
  <p class="welcome-text abs">Lorem Ipsum is simply dummy text of the printing and typesetting industry. Lorem Ipsum has been the industry's standard dummy text ever since the 1500s, when an unknown printer took a galley of type and scrambled it to make a type specimen book. It has survived not only five centuries, but also the leap into electronic typesetting, remaining essentially unchanged.</p>
  <div class="contact-box abs"></div>
  <div class="contact-icon abs" style="left:99px;top:466px"><svg width="12" height="12" viewBox="0 0 24 24"><path fill="#1a73c1" d="M6.6 10.8a15 15 0 0 0 6.6 6.6l2.2-2.2c.3-.3.7-.4 1-.2 1.1.4 2.3.6 3.6.6.6 0 1 .4 1 1V20c0 .6-.4 1-1 1A17 17 0 0 1 3 4c0-.6.4-1 1-1h3.5c.6 0 1 .4 1 1 0 1.3.2 2.5.6 3.6.1.3 0 .7-.2 1z"/></svg></div>
  <span class="contact-label abs" style="left:132px;top:464px">Phone:</span>
  <span class="contact-value abs" style="left:132px;top:474px">000-000-0000</span>
  <div class="abs" style="left:208px;top:464px;width:1px;height:28px;background:#ccc"></div>
  <div class="contact-icon abs" style="left:216px;top:466px"><svg width="13" height="10" viewBox="0 0 26 20"><rect width="26" height="20" fill="#1a73c1"/><path d="M1 1 13 11 25 1" fill="none" stroke="#fff" stroke-width="2"/></svg></div>
  <span class="contact-label abs" style="left:249px;top:464px">email:</span>
  <span class="abs" style="left:249px;top:477px;font-size:7.5px;color:#333">info@harlowdata.com</span>

  <div class="quote abs" role="img" aria-label="Blue tinted photo of hands reviewing printed charts"></div>
  <h2 class="quote-title abs">GET A QUOTE!</h2>
  <p class="quote-sub abs">Fill all information field bellow.</p>
  <div class="field abs" style="top:375px;height:17px">Enter your name</div>
  <div class="field abs" style="top:397px;height:16px">Enter your email</div>
  <div class="field abs" style="top:418px;height:17px">Enter your Phone</div>
  <div class="field abs" style="top:440px;height:42px">Comments</div>
  <div class="submit abs">SUBMIT</div>
</section>

<section>
  <div class="title-line abs" style="left:140px;top:557px;width:116px"></div>
  <div class="title-sq abs" style="left:260px;top:552px"></div>
  <h2 class="section-title abs" style="top:546px">OUR SERVICES</h2>
  <div class="title-sq abs" style="left:423px;top:552px"></div>
  <div class="title-line abs" style="left:438px;top:557px;width:114px"></div>
  <div class="title-under abs" style="top:576px"></div>

  <article class="card abs" style="left:93px">
    <div class="card-icon"><svg width="16" height="18" viewBox="0 0 16 18" fill="#fff"><ellipse cx="8" cy="3" rx="7" ry="2.5"/><path d="M1 5c0 1.4 3 2.5 7 2.5S15 6.4 15 5v3c0 1.4-3 2.5-7 2.5S1 9.4 1 8zM1 10c0 1.4 3 2.5 7 2.5s7-1.1 7-2.5v3c0 1.4-3 2.5-7 2.5S1 14.4 1 13z"/></svg></div>
    <h3 class="card-title">DATA GOVERNANCE</h3><div class="card-rule"></div>
    <p class="card-text">Lorem Ipsum is simply dummy text of the printing and typesetting industry.</p>
  </article>
  <article class="card abs" style="left:220px">
    <div class="card-icon"><svg width="16" height="18" viewBox="0 0 16 18"><rect x="2" y="1" width="11" height="15" fill="none" stroke="#fff" stroke-width="1.4"/><path d="M4.5 5h6M4.5 8h6M4.5 11h4" stroke="#fff" stroke-width="1.2"/><path d="m10 14 5-6" stroke="#fff" stroke-width="1.6"/></svg></div>
    <h3 class="card-title">REPORT MODELLING</h3><div class="card-rule"></div>
    <p class="card-text">Lorem Ipsum is simply dummy text of the printing and typesetting industry.</p>
  </article>
  <article class="card abs" style="left:348px">
    <div class="card-icon"><svg width="14" height="18" viewBox="0 0 14 18" fill="#fff"><path d="M7 1a6 6 0 0 0-3.5 10.8V14h7v-2.2A6 6 0 0 0 7 1z"/><rect x="4" y="15" width="6" height="2"/><circle cx="7" cy="7" r="2" fill="#1a73c1"/></svg></div>
    <h3 class="card-title">BUSINESS INTELLIGENCE</h3><div class="card-rule"></div>
    <p class="card-text">Lorem Ipsum is simply dummy text of the printing and typesetting industry.</p>
  </article>
  <article class="card abs" style="left:476px">
    <div class="card-icon"><svg width="18" height="18" viewBox="0 0 18 18" fill="#fff"><ellipse cx="7" cy="3" rx="6" ry="2.2"/><path d="M1 5c0 1.2 2.7 2.2 6 2.2S13 6.2 13 5v3c0 1.2-2.7 2.2-6 2.2S1 9.2 1 8zM1 10c0 1.2 2.7 2.2 6 2.2v3C3.7 15.2 1 14.2 1 13z"/><circle cx="13" cy="13" r="4"/><path d="m11.2 13 1.3 1.3 2.3-2.5" fill="none" stroke="#1a73c1" stroke-width="1.2"/></svg></div>
    <h3 class="card-title">DATA PROTECTION</h3><div class="card-rule"></div>
    <p class="card-text">Lorem Ipsum is simply dummy text of the printing and typesetting industry.</p>
  </article>
  <div class="divider abs"></div>
  <svg class="abs" style="left:339px;top:704px" width="14" height="7" viewBox="0 0 14 7"><path d="M0 0 7 6 14 0" fill="#fff" stroke="#b7d3ea"/></svg>
</section>

<section>
  <div class="cta abs"></div>
  <div class="cta-icon abs"><svg width="18" height="14" viewBox="0 0 18 14"><path d="M1 5c0-3 16-3 16 0v1.5h-4V4.5H5v2H1z" fill="#fff"/><path d="M4 7h10l2 6H2z" fill="#fff"/><circle cx="9" cy="10" r="2" fill="#1c6aae"/></svg></div>
  <h2 class="cta-title abs">Got Questions?Need Answers?</h2>
  <p class="cta-sub abs">Contact a customer service representative now.</p>
</section>

<section>
  <div class="title-line abs" style="left:140px;top:825px;width:116px"></div>
  <div class="title-sq abs" style="left:260px;top:820px"></div>
  <h2 class="section-title abs" style="top:814px">TESTIMONIALS</h2>
  <div class="title-sq abs" style="left:423px;top:820px"></div>
  <div class="title-line abs" style="left:438px;top:825px;width:114px"></div>
  <div class="title-under abs" style="top:844px"></div>

  <div class="testimonial abs" style="left:112px"></div>
  <span class="quote-mark abs" style="left:128px">&ldquo;</span>
  <p class="testimonial-text abs" style="left:129px">Lorem Ipsum is simply dummy text of the printing and typesetting industry. Lorem Ipsum has been the industry's standard dummy text ever since the 1500s, when an unknown printer took ...</p>
  <svg class="abs" style="left:142px;top:940px" width="14" height="8" viewBox="0 0 14 8"><path d="M0 0 7 7 14 0" fill="#f2f2f2" stroke="#a9c6e0"/></svg>
  <div class="avatar abs" style="left:130px;top:959px" role="img" aria-label="Client portrait"></div>
  <span class="person abs" style="left:177px;top:965px">Peter Ashby</span>
  <span class="role abs" style="left:177px;top:978px">Happy Clients</span>

  <div class="testimonial abs" style="left:356px"></div>
  <span class="quote-mark abs" style="left:378px">&ldquo;</span>
  <p class="testimonial-text abs" style="left:380px;width:180px">Lorem Ipsum is simply dummy text of the printing and typesetting industry. Lorem Ipsum has been the industry's standard dummy...</p>
  <svg class="abs" style="left:386px;top:940px" width="14" height="8" viewBox="0 0 14 8"><path d="M0 0 7 7 14 0" fill="#f2f2f2" stroke="#a9c6e0"/></svg>
  <div class="avatar abs" style="left:375px;top:959px" role="img" aria-label="Client portrait"></div>
  <span class="person abs" style="left:422px;top:965px">Peter Ashby</span>
  <span class="role abs" style="left:422px;top:978px">Happy Clients</span>
</section>

<footer>
  <div class="footer abs"></div>
  <h3 class="footer-head abs" style="left:93px">About Us:</h3>
  <div class="footer-rule abs" style="left:93px;top:1061px;width:165px"></div>
  <p class="footer-text abs" style="left:93px;top:1071px;width:168px">Lorem Ipsum is simply dummy text of the printing and typesetting industry. Lorem Ipsum has been the industry's standard dummy text ever since the 1500s, when an unknown printer took a galley of type and scrambled it to make a type specimen book. It has survived not only...</p>
  <div class="footer-rule abs" style="left:93px;top:1129px;width:165px"></div>
  <span class="abs" style="left:93px;top:1140px;font-size:9px;color:#fff">Connect with us</span>
  <span class="social abs" style="left:165px"></span>
  <span class="social abs" style="left:184px"></span>
  <span class="social abs" style="left:203px"></span>

  <h3 class="footer-head abs" style="left:292px">Contact Information:</h3>
  <div class="footer-rule abs" style="left:292px;top:1061px;width:132px"></div>
  <div class="footer-item abs" style="top:1067px"><svg width="9" height="9" viewBox="0 0 10 10"><rect width="10" height="10" rx="1" fill="#fff"/><path d="M3 2.5c0 2.5 2 4.5 4.5 4.5l.5-1.2-1.3-.6-.6.6A3 3 0 0 1 4.7 4.4l.6-.6-.6-1.3z" fill="#0b3553"/></svg>Call: 000-000-0000</div>
  <div class="footer-item abs" style="top:1086px"><svg width="9" height="7" viewBox="0 0 10 8"><rect width="10" height="8" fill="#fff"/><path d="M0 0 5 4 10 0" fill="none" stroke="#0b3553"/></svg>email: <small>info@harlowdata.com</small></div>
  <div class="footer-item abs" style="top:1104px"><svg width="9" height="9" viewBox="0 0 10 10"><circle cx="5" cy="5" r="4.5" fill="#fff"/><path d="M.5 5h9M5 .5c-2.5 3-2.5 6 0 9M5 .5c2.5 3 2.5 6 0 9" fill="none" stroke="#0b3553" stroke-width=".8"/></svg>website: <small>www.harlowdata.com</small></div>

  <h3 class="footer-head abs" style="left:467px">Newsletter</h3>
  <div class="footer-rule abs" style="left:467px;top:1061px;width:132px"></div>
  <div class="news-input abs">Enter Your Email Id</div>
  <div class="subscribe abs">SUBSCRIBE</div>

  <div class="footer-bar abs">© Copyright 2017 Harlow Data.com. All Rights Reserved</div>
</footer>

</body>
</html>
```